KRV Business cards
Cards
Simple
Gareth Pullman
President
7408 19th St, NW
Washington, DC 20093
gpullman@KRVantage.com
www.KRVantage.com
Please include tag line
LAUNCH | ACCELERATE | IMPROVE
Marketing and Business Consultants
-Strategy
-Business mentoring
-Sales & marketing
-Web design & e-marketing
-New product introductions
-Customer satisfaction
Logo for business cards - ai
logo for business cards - eps
file for Rovendra
file for rovendra #2

```html
<!DOCTYPE html>
<html lang="en">
<head>
<meta charset="utf-8">
<title>KRV Business Cards</title>
<link href="https://fonts.googleapis.com/css2?family=Roboto+Condensed:wght@400;700&display=swap" rel="stylesheet">
<style>
  :root {
    --stage: #000000;
    --blue-deep: #0a5fb4;
    --blue-mid: #1787da;
    --blue-light: #3fa9ee;
    --logo-blue: #1a7fd0;
    --white: #ffffff;
    --ink: #1a1a1a;
  }
  * { margin: 0; padding: 0; box-sizing: border-box; }
  html, body { width: 1200px; height: 1055px; overflow: hidden; background: var(--stage); }
  body { position: relative; font-family: "Roboto Condensed", Arial, sans-serif; }

  .card {
    position: absolute;
    left: 265px;
    width: 685px;
    height: 394px;
    overflow: hidden;
  }
  .card-front { top: 142px; background: linear-gradient(135deg, var(--blue-light), var(--blue-mid) 45%, var(--blue-deep)); }
  .card-back {
    top: 547px;
    background: radial-gradient(ellipse at 50% 40%, var(--blue-light), var(--blue-mid) 50%, var(--blue-deep));
    color: var(--white);
    text-align: center;
  }
  .front-shape { position: absolute; inset: 0; }

  .brand-name {
    position: absolute;
    left: 78px; top: 28px;
    font-size: 100px;
    font-weight: 700;
    letter-spacing: 14px;
    color: var(--logo-blue);
    line-height: 1;
  }

  .holder { position: absolute; right: 36px; top: 48px; text-align: right; color: var(--white); }
  .holder-name { font-size: 28px; font-weight: 700; line-height: 1.1; }
  .holder-title { font-size: 25px; line-height: 1.1; }

  .contact { position: absolute; right: 36px; top: 158px; text-align: right; color: var(--white); font-size: 19px; line-height: 1.4; }
  .contact-row { display: flex; justify-content: flex-end; align-items: center; gap: 6px; }
  .contact-icon { width: 16px; height: 16px; }

  .tagline {
    position: absolute; right: 36px; top: 347px;
    color: var(--white); font-size: 23px; font-weight: 700; letter-spacing: 0.5px;
  }
  .tagline .sep { font-size: 16px; margin: 0 4px; vertical-align: 2px; }

  .service-heading { margin-top: 40px; font-size: 23px; font-weight: 700; line-height: 1.4; }
  .service-list { list-style: none; margin-top: 12px; font-size: 19px; line-height: 31px; }
  .glow-line {
    position: absolute; left: 60px; right: 60px; bottom: 60px; height: 2px;
    background: linear-gradient(90deg, transparent, rgba(255,255,255,0.35), transparent);
  }
</style>
</head>
<body>
  <section class="card card-front">
    <svg class="front-shape" viewBox="0 0 685 394" preserveAspectRatio="none" aria-hidden="true">
      <path d="M0,0 H430 C370,10 352,70 348,140 C342,240 318,305 248,342 C190,372 110,394 0,394 Z" fill="#ffffff"/>
      <path d="M430,0 C370,10 352,70 348,140 C342,240 318,305 248,342" fill="none" stroke="#0a5fb4" stroke-opacity="0.35" stroke-width="6"/>
    </svg>
    <div class="brand-name">KRV</div>

    <div class="holder">
      <div class="holder-name">Gareth Pullman</div>
      <div class="holder-title">President</div>
    </div>

    <div class="contact">
      <div>7408 19th St, NW</div>
      <div>Washington, DC 20093</div>
      <div class="contact-row">
        <svg class="contact-icon" viewBox="0 0 16 16"><circle cx="8" cy="8" r="7.5" fill="#fff"/><path d="M5 4.5l1.5-.5 1 2-1 .8c.5 1 1.2 1.7 2.2 2.2l.8-1 2 1-.5 1.5c-3 .3-6.3-3-6-6z" fill="#1787da"/></svg>
        <span>: 202.555.0143</span>
      </div>
      <div class="contact-row">
        <svg class="contact-icon" viewBox="0 0 16 16"><rect x="2" y="3" width="12" height="10" fill="#fff"/><path d="M2 3l6 5 6-5" fill="none" stroke="#1787da" stroke-width="1.2"/></svg>
        <span>: gpullman@KRVantage.com</span>
      </div>
      <div class="contact-row">
        <svg class="contact-icon" viewBox="0 0 16 16"><circle cx="8" cy="8" r="7" fill="#fff"/><ellipse cx="8" cy="8" rx="3" ry="7" fill="none" stroke="#1787da"/><path d="M1 8h14" stroke="#1787da"/></svg>
        <span>: www.KRVantage.com</span>
      </div>
    </div>

    <div class="tagline">LAUNCH<span class="sep">◆</span>ACCELERATE<span class="sep">◆</span>IMPROVE</div>
  </section>

  <section class="card card-back">
    <h2 class="service-heading">MARKETING<br>&amp; BUSINESS CONSULTANTS</h2>
    <ul class="service-list">
      <li>Strategy</li>
      <li>Business mentoring</li>
      <li>Sales &amp; marketing</li>
      <li>Web design &amp; e-marketing</li>
      <li>New product introductions</li>
      <li>Customer satisfaction</li>
    </ul>
    <div class="glow-line"></div>
  </section>
</body>
</html>
```